Design a Wordpress based website for selling Tiny homes

Needs to be Wordpress based. 3-4 pages of content. I will be supplying most of the pictures, the other images can be stock.

Target Market(s)

Young couples, students, mum/dad, property developers

Industry/Entity Type

Home Builder

Logo Text

Your dream tiny house

Coding

Coded - Design and coding required

Number of Pages Required

4 page

Colors

Designer to choose colors to be used in the design.

Requirements
Must have
• Top menu must have (Home, Models, Tiny Homes, Order). See "Capture.JPEG" and link for text/script to copy - https://example-tinyhaven.net/site-1
• Logo should be based on the text "Your dream tiny house"
Nice to have
• Similar positioning of text and layout to what the "Capture.jpeg" has OR better.

```html
<!DOCTYPE html>
<html lang="en">
<head>
<meta charset="utf-8">
<title>Tiny Haven Homes</title>
<link rel="stylesheet" href="https://fonts.googleapis.com/css2?family=Nunito:wght@600;700;800&family=Roboto:wght@400;500&display=swap">
<style>
:root{
  --blue:#1a4ad6;
  --blue-deep:#10308f;
  --navy:#0f2a8a;
  --orange:#e8601c;
  --ink:#1d1d1f;
  --field:#efefef;
  --footer:#dde2f1;
  --white:#fff;
}
*{margin:0;padding:0;box-sizing:border-box}
html,body{width:1200px;height:2987px;overflow:hidden}
body{position:relative;background:var(--white);font-family:"Roboto",sans-serif;color:var(--ink)}
.abs{position:absolute}

/* header */
.site-header{position:absolute;left:0;top:0;width:1200px;height:96px;background:var(--white)}
.brand{position:absolute;left:44px;top:22px;display:flex;align-items:center;gap:12px}
.brand-mark{width:40px;height:40px;border:3px solid var(--blue);border-radius:4px}
.brand-name{font-family:"Nunito",sans-serif;font-weight:800;font-size:25px;line-height:27px;color:var(--blue);letter-spacing:.5px;text-transform:uppercase}
.main-nav{position:absolute;top:44px;left:590px;display:flex;gap:37px;font-family:"Nunito",sans-serif;font-weight:700;font-size:17px;color:var(--ink)}
.main-nav .current{color:var(--blue);position:relative}
.home-icon{position:absolute;left:-12px;top:-18px}

/* hero */
.hero{position:absolute;left:0;top:96px;width:1200px;height:607px;
  background:radial-gradient(ellipse at 50% 60%,#8a4a1c 0%,#4a2a1e 35%,#1c1738 75%,#12122a 100%)}
.hero h1{position:absolute;left:0;right:0;top:188px;text-align:center;font-family:"Nunito",sans-serif;font-weight:800;font-size:47px;line-height:48px;color:var(--white);text-transform:uppercase}
.hero .chevron{position:absolute;left:571px;top:370px}

/* models */
.section-title{position:absolute;left:0;right:0;text-align:center;font-family:"Nunito",sans-serif;font-weight:800;font-size:37px;text-transform:uppercase}
.section-title::after{content:"";display:block;width:87px;height:4px;background:var(--blue);margin:10px auto 0}
.models-title{top:762px;color:var(--blue)}
.model-card{position:absolute;top:858px;width:275px;height:361px;border:1px solid #cfcfcf;border-radius:3px;background:var(--white);overflow:hidden}
.model-photo{height:203px}
.model-name{position:absolute;left:30px;top:222px;font-family:"Nunito",sans-serif;font-weight:700;font-size:24px;color:var(--blue)}
.model-style{position:absolute;left:31px;top:255px;font-family:"Nunito",sans-serif;font-weight:600;font-size:19px;color:var(--ink)}
.btn-more{position:absolute;left:28px;top:298px;height:37px;padding:0 25px;border-radius:19px;background:var(--orange);color:var(--white);font-size:12px;font-weight:500;line-height:37px;text-transform:uppercase}

/* about */
.about{position:absolute;left:0;top:1316px;width:1200px;height:614px}
.about-panel{position:absolute;left:0;top:0;width:603px;height:614px;background:linear-gradient(180deg,var(--blue) 0%,var(--blue) 45%,var(--blue-deep) 100%)}
.about-photo{position:absolute;left:603px;top:0;width:597px;height:614px;background:linear-gradient(160deg,#3d3a2a 0%,#a35a2a 40%,#c7783c 70%,#5b3a22 100%)}
.about h2{position:absolute;left:166px;top:72px;font-family:"Nunito",sans-serif;font-weight:800;font-size:37px;color:var(--white)}
.about h2::after{content:"";display:block;width:87px;height:4px;background:var(--white);margin-top:6px}
.about p{position:absolute;left:166px;top:150px;width:380px;font-size:16px;line-height:28px;color:var(--white)}
.perks{position:absolute;left:164px;top:266px;list-style:none;font-size:20px;color:var(--white)}
.perks li{height:40.5px;display:flex;align-items:center;gap:6px}

/* contact */
.contact-title{top:1990px;color:var(--ink)}
.map{position:absolute;left:165px;top:2080px;width:865px;height:349px;background:linear-gradient(135deg,#ececec,#f6f6f6 50%,#e6e6e6)}
.col-title{position:absolute;top:2462px;font-family:"Nunito",sans-serif;font-weight:700;font-size:26px;color:var(--ink);text-transform:uppercase}
.field{position:absolute;left:176px;width:405px;height:43px;background:var(--field);font-size:14px;padding:14px 26px;color:var(--ink)}
.btn-submit{position:absolute;left:434px;top:2775px;width:147px;height:44px;background:var(--orange);color:var(--white);font-family:"Nunito",sans-serif;font-weight:700;font-size:17px;text-align:center;line-height:44px}
.touch{position:absolute;left:655px;top:2520px;list-style:none;font-size:17px;color:var(--ink)}
.touch li{height:36px;line-height:36px}
.quote{position:absolute;left:656px;top:2728px;font-family:"Nunito",sans-serif;font-weight:800;font-size:24px;color:var(--navy)}

/* footer */
.site-footer{position:absolute;left:0;top:2894px;width:1200px;height:93px;background:var(--footer)}
.copyright{position:absolute;left:180px;top:36px;font-size:14px;color:var(--ink)}
.social{position:absolute;left:866px;top:27px;display:flex;gap:9px}
.social span{width:35px;height:35px;border-radius:50%;background:var(--navy)}
</style>
</head>
<body>

<header class="site-header">
  <div class="brand"><span class="brand-mark"></span><span class="brand-name">Tiny Haven<br>Homes</span></div>
  <nav class="main-nav">
    <span class="current"><svg class="home-icon" width="26" height="34" viewBox="0 0 26 34"><path d="M2 32V14L13 3l11 11" fill="none" stroke="#1a4ad6" stroke-width="2.5"/></svg>HOME</span>
    <span>MODELS</span><span>TINY HOMES</span><span>ORDER</span><span>CONTACT US</span>
  </nav>
</header>

<section class="hero">
  <div class="abs" style="inset:0" role="img" aria-label="Wooden tiny house at night with string lights in a backyard"></div>
  <h1>Stunning house in<br>your backyard in the<br>heart of your city</h1>
  <svg class="chevron" width="58" height="32" viewBox="0 0 58 32"><path d="M2 2l27 27L56 2" fill="none" stroke="#fff" stroke-width="3" opacity=".85"/></svg>
</section>

<h2 class="section-title models-title">Tiny Home Models</h2>

<article class="model-card" style="left:166px">
  <div class="model-photo" style="background:linear-gradient(180deg,#cfd6de,#e3b92a 55%,#5a4a2a)" role="img" aria-label="Yellow tiny home on a trailer"></div>
  <h3 class="model-name">Roger Tiny Home</h3>
  <p class="model-style">Yellow Forest</p>
  <span class="btn-more">Learn more</span>
</article>
<article class="model-card" style="left:465px">
  <div class="model-photo" style="background:linear-gradient(180deg,#7e9bc4,#9a6a3a 50%,#4a3a2a)" role="img" aria-label="Timber-clad tiny home in a country field"></div>
  <h3 class="model-name" style="left:24px">Coutry Free</h3>
  <p class="model-style" style="left:26px;top:253px">Country</p>
  <span class="btn-more" style="left:24px;top:294px">Learn more</span>
</article>
<article class="model-card" style="left:764px">
  <div class="model-photo" style="background:linear-gradient(180deg,#b9c8a8,#b8402a 40%,#8a2c1e 85%,#333)" role="img" aria-label="Red tiny home on a trailer"></div>
  <h3 class="model-name" style="left:37px;top:224px">Lagoon</h3>
  <p class="model-style" style="left:38px;top:256px">Lagoon Red</p>
  <span class="btn-more" style="left:35px;top:296px">Learn more</span>
</article>

<section class="about">
  <div class="about-panel"></div>
  <div class="about-photo" role="img" aria-label="Cedar tiny home with glass double doors"></div>
  <h2>ABOUT US</h2>
  <p>Pellentesque faucibus Ut accumsan ultricies elit Maecenas at justo id velit placerat molestie Donec dictum lectus non odio Cras a ante vitae enim</p>
  <ul class="perks">
    <li><svg width="20" height="20" viewBox="0 0 20 20"><circle cx="10" cy="10" r="9.5" fill="#fff"/><path d="M5.5 10.5l3 3 6-6.5" fill="none" stroke="#1a4ad6" stroke-width="2.4"/></svg>Affordability</li>
    <li><svg width="20" height="20" viewBox="0 0 20 20"><circle cx="10" cy="10" r="9.5" fill="#fff"/><path d="M5.5 10.5l3 3 6-6.5" fill="none" stroke="#1a4ad6" stroke-width="2.4"/></svg>Compact size</li>
    <li><svg width="20" height="20" viewBox="0 0 20 20"><circle cx="10" cy="10" r="9.5" fill="#fff"/><path d="M5.5 10.5l3 3 6-6.5" fill="none" stroke="#1a4ad6" stroke-width="2.4"/></svg>Ease of installation</li>
    <li><svg width="20" height="20" viewBox="0 0 20 20"><circle cx="10" cy="10" r="9.5" fill="#fff"/><path d="M5.5 10.5l3 3 6-6.5" fill="none" stroke="#1a4ad6" stroke-width="2.4"/></svg>Cute appearance</li>
    <li><svg width="20" height="20" viewBox="0 0 20 20"><circle cx="10" cy="10" r="9.5" fill="#fff"/><path d="M5.5 10.5l3 3 6-6.5" fill="none" stroke="#1a4ad6" stroke-width="2.4"/></svg>Can earn you money</li>
    <li><svg width="20" height="20" viewBox="0 0 20 20"><circle cx="10" cy="10" r="9.5" fill="#fff"/><path d="M5.5 10.5l3 3 6-6.5" fill="none" stroke="#1a4ad6" stroke-width="2.4"/></svg>Quick to get on your land</li>
    <li><svg width="20" height="20" viewBox="0 0 20 20"><circle cx="10" cy="10" r="9.5" fill="#fff"/><path d="M5.5 10.5l3 3 6-6.5" fill="none" stroke="#1a4ad6" stroke-width="2.4"/></svg>Extra income</li>
  </ul>
</section>

<h2 class="section-title contact-title">Contact Us</h2>
<div class="map" role="img" aria-label="Street map of the office location in central Sydney"></div>

<h3 class="col-title" style="left:176px">Inquiries</h3>
<div class="field" style="top:2518px">Name</div>
<div class="field" style="top:2569px">Email</div>
<div class="field" style="top:2620px">Phone</div>
<div class="field" style="top:2670px;height:93px">Message</div>
<div class="btn-submit">SUBMIT</div>

<h3 class="col-title" style="left:651px">Get in touch</h3>
<ul class="touch">
  <li>level 12- 48 Harbour Lane Sydney</li>
  <li>2000 NSW Australia</li>
  <li>hello@tinyhaven-example.net</li>
  <li>Tel: +61-2-5550 1408</li>
  <li>Fax: +61-2-5550 1499</li>
</ul>
<p class="quote">Get a quote: 555-010-2468</p>

<footer class="site-footer">
  <p class="copyright">© 2019 Company Name&nbsp; All right reserved</p>
  <div class="social"><span></span><span></span><span></span><span></span></div>
</footer>

</body>
</html>
```